Communications & Broadcast Consulting/PR/Media Relations & Public Affairs

My main goals are to provide communications support to school districts, small towns/cities/hospitals and private businesses in the form of press releases, media relations, public affairs. I also have 25 years experience as a television news anchor/reporter and I'm open to free-lance reporting in both Indianapolis and other markets. My specialty is working with the media.
Communications

```html
<!DOCTYPE html>
<html lang="en">
<head>
<meta charset="UTF-8">
<title>Business Card</title>
<link rel="stylesheet" href="https://fonts.googleapis.com/css2?family=Marcellus&family=Tinos&display=swap">
<style>
  :root {
    --backdrop: #6e7a86;
    --card: #ffffff;
    --accent-red: #850010;
    --bar-grey: #6b6b6b;
    --ink: #111111;
    --name-ink: #ffffff;
  }
  * { margin: 0; padding: 0; box-sizing: border-box; }
  html, body {
    width: 1200px;
    height: 1000px;
    overflow: hidden;
    background: var(--backdrop);
  }
  .canvas {
    position: relative;
    width: 1200px;
    height: 1000px;
  }
  .business-card {
    position: absolute;
    left: 75px;
    top: 200px;
    width: 1050px;
    height: 600px;
    background: var(--card);
    box-shadow: 0 10px 30px rgba(0,0,0,0.25);
  }
  .name-band {
    position: absolute;
    left: 0;
    top: 260px;
    width: 480px;
    height: 150px;
    background: var(--accent-red);
    display: flex;
    align-items: center;
    padding-left: 100px;
  }
  .person-name {
    font-family: "Marcellus", serif;
    font-size: 58px;
    color: var(--name-ink);
    letter-spacing: 1px;
    white-space: nowrap;
  }
  .contact-list {
    position: absolute;
    left: 525px;
    top: 205px;
    list-style: none;
    font-family: "Tinos", serif;
    font-size: 29px;
    line-height: 44px;
    color: var(--ink);
    white-space: nowrap;
  }
  .contact-label { margin-right: 6px; }
  .accent-bars {
    position: absolute;
    top: 78px;
    left: 0;
    width: 100%;
  }
  .accent-bar {
    position: absolute;
    width: 150px;
    height: 30px;
    background: var(--bar-grey);
  }
  .accent-bar:nth-child(1) { left: 700px; top: 0; }
  .accent-bar:nth-child(2) { left: 730px; top: 40px; }
  .accent-bar:nth-child(3) { left: 760px; top: 80px; }
  .accent-bar:nth-child(4) { left: 790px; top: 120px; }
</style>
</head>
<body>
  <main class="canvas">
    <section class="business-card">
      <div class="accent-bars" aria-hidden="true">
        <span class="accent-bar"></span>
        <span class="accent-bar"></span>
        <span class="accent-bar"></span>
        <span class="accent-bar"></span>
      </div>
      <ul class="contact-list">
        <li><span class="contact-label">P :</span>012- 345- 6789</li>
        <li><span class="contact-label">E :</span>your name@mail.com</li>
        <li><span class="contact-label">W :</span>www.address.com</li>
      </ul>
      <div class="name-band">
        <h1 class="person-name">Your Name</h1>
      </div>
    </section>
  </main>
</body>
</html>
```